Silver Harbor Dental Clinic Flyer

I need to make a flyer Design for my clinic (Silver Harbor Dental Clinic) Based in Philippines, Makati .
We are Providing dental Service for high end market in the Philippines. Our speciality is Dental Aesthetic/Beautification. Our targets are actors/actresses, athletes, middle to high end
We are going to place this flyers in places like Ridgeway Fitness . and other lifestyle related places

Target Market(s)

Mid to high market

Industry/Entity Type

Dental Clinic

Font styles to use
Serif

Requirements
Must have
• The flyer should Contain Our address and the services that we offer
• #4821 Orchid Tower Makati Dalisay Cor. Verano St. Lumen Square .Makati
• Email: info@silverharbor.example.ph
• mobile +639051274806
• Landline:(02)5162947
• instagram:@shdc.ph
• facebook:SHDC.ph
• Our Services :
• General Dentistry ,Orthodontics ,Cosmetic Dentistry ,Pediatric Dentistry ,Teeth Whitening,Dental Implants ,Wisdom Tooth Extraction,Root Canal Therapy
• Silver Harbor Kids Treatment:
• Teeth Cleaning , Flouride Application ,Tooth Colored Filing ,Extraction ,Pit and Fissure Sealants, Space Management
Nice to have
• Nice to have a nice tagline

```html
<!DOCTYPE html>
<html lang="en">
<head>
<meta charset="utf-8">
<title>Silver Harbor Dental Clinic Flyer</title>
<link href="https://fonts.googleapis.com/css2?family=Hind:wght@600;700&family=Quicksand:wght@500;600;700&display=swap" rel="stylesheet">
<style>
:root{
  --page:#e9ebea;
  --paper:#f6f7f7;
  --ink-dark:#1f2523;
  --sage:#5f736d;
  --sage-light:#80948e;
  --teal-text:#7fa19a;
  --white:#ffffff;
  --photo-a:#c9d3dc;
  --photo-b:#e8e2dc;
}
*{margin:0;padding:0;box-sizing:border-box}
html,body{width:1200px;height:1200px;overflow:hidden;background:var(--page)}
.flyer{position:absolute;left:180px;top:18px;width:860px;height:1192px;transform:scale(0.9765);transform-origin:0 0;background:var(--paper);overflow:hidden;box-shadow:0 4px 18px rgba(0,0,0,.12)}
.shapes{position:absolute;inset:0}
.photo{position:absolute}
.photo--man{left:0;top:0;width:430px;height:350px;background:linear-gradient(160deg,var(--photo-b),var(--photo-a));clip-path:polygon(0 0,380px 0,428px 350px,0 350px)}
.photo--couple{left:0;top:0;width:860px;height:350px;background:linear-gradient(200deg,#f1ece8,#d9c7b8);clip-path:polygon(390px 0,860px 0,860px 350px,438px 350px)}
.photo--child{left:592px;top:815px;width:284px;height:284px;border-radius:50%;background:radial-gradient(circle at 45% 45%,#f3e3dc,#c9b6ad)}
.brand{position:absolute;left:100px;top:455px;width:250px;display:flex;align-items:center;gap:10px;font-family:"Quicksand",sans-serif;font-weight:600;font-size:24px;color:var(--sage-light)}
.brand__dot{width:14px;height:14px;border-radius:50%;background:var(--sage-light);flex:none}
.tagline{position:absolute;left:60px;top:562px;font-family:"Hind",sans-serif;font-weight:700;line-height:1;font-size:56px;color:var(--white)}
.tagline__accent{display:block;color:var(--teal-text);margin-top:6px}
.services{position:absolute;left:470px;top:418px;font-family:"Quicksand",sans-serif;color:var(--white)}
.services__title{font-weight:700;font-size:25px;margin-bottom:10px}
.check-list{list-style:none}
.check-list li{display:flex;align-items:center;gap:10px;font-weight:500}
.services .check-list li{font-size:20.5px;height:30.7px}
.tick{width:18px;height:18px;flex:none}
.kids{position:absolute;left:54px;top:882px;font-family:"Quicksand",sans-serif;color:var(--ink-dark)}
.kids__title{font-family:"Hind",sans-serif;font-weight:700;font-size:20px;margin-bottom:18px}
.kids__cols{display:flex;gap:28px}
.kids .check-list li{font-size:19.5px;height:30px}
.footer{position:absolute;left:38px;top:1132px;font-family:"Quicksand",sans-serif;font-weight:500;font-size:12.5px;line-height:16px;color:var(--white)}
.footer__social{display:inline-flex;align-items:center;gap:4px}
.footer__mark{display:inline-block;width:10px;height:10px;background:var(--white)}
</style>
</head>
<body>
<div class="flyer">
  <div class="photo photo--couple" role="img" aria-label="Photo of a laughing young couple embracing"></div>
  <div class="photo photo--man" role="img" aria-label="Photo of a smiling grey-haired man resting chin on hand"></div>

  <svg class="shapes" viewBox="0 0 860 1192" width="860" height="1192" aria-hidden="true">
    <defs>
      <linearGradient id="sageGrad" x1="0" y1="0" x2="1" y2="1">
        <stop offset="0" stop-color="#6c807a"/>
        <stop offset="1" stop-color="#4f625c"/>
      </linearGradient>
      <linearGradient id="darkGrad" x1="0" y1="0" x2="0" y2="1">
        <stop offset="0" stop-color="#262d2b"/>
        <stop offset="1" stop-color="#1a201e"/>
      </linearGradient>
    </defs>
    <path d="M0 300 C200 290 400 318 560 344 L860 344 L860 808 C700 838 520 852 380 838 C220 822 90 744 0 660 Z" fill="var(--white)"/>
    <path d="M0 310 C200 298 400 326 560 352 L860 352 L860 800 C700 830 520 845 380 830 C220 814 90 738 0 652 Z" fill="url(#darkGrad)"/>
    <path d="M433 776 L433 420 C470 370 560 330 790 292 L790 660 C740 732 620 768 433 776 Z" fill="var(--white)"/>
    <path d="M433 768 L433 424 C472 378 562 340 790 302 L790 656 C738 724 620 760 433 768 Z" fill="url(#sageGrad)"/>
    <path d="M0 1048 C200 1086 400 1088 500 1034" fill="none" stroke="var(--ink-dark)" stroke-width="6"/>
    <path d="M0 1192 L0 1080 C250 1112 500 1100 860 1040 L860 1192 Z" fill="url(#sageGrad)"/>
    <circle cx="734" cy="957" r="166" fill="var(--sage)"/>
    <circle cx="734" cy="957" r="152" fill="var(--white)"/>
  </svg>

  <div class="photo photo--child" role="img" aria-label="Photo of a smiling curly-haired little girl with hands on cheeks"></div>

  <div class="brand"><span class="brand__dot"></span>Silver Harbor</div>

  <h1 class="tagline">Bringing life<span class="tagline__accent">to your smile</span></h1>

  <section class="services">
    <h2 class="services__title">Our Services :</h2>
    <ul class="check-list">
      <li><svg class="tick" viewBox="0 0 18 18"><circle cx="9" cy="9" r="9" fill="#fff"/><path d="M5 9.2l2.7 2.6L13 6.4" fill="none" stroke="#5f736d" stroke-width="2.2"/></svg>General Dentistry</li>
      <li><svg class="tick" viewBox="0 0 18 18"><circle cx="9" cy="9" r="9" fill="#fff"/><path d="M5 9.2l2.7 2.6L13 6.4" fill="none" stroke="#5f736d" stroke-width="2.2"/></svg>Orthodontics</li>
      <li><svg class="tick" viewBox="0 0 18 18"><circle cx="9" cy="9" r="9" fill="#fff"/><path d="M5 9.2l2.7 2.6L13 6.4" fill="none" stroke="#5f736d" stroke-width="2.2"/></svg>Cosmetic Dentistry</li>
      <li><svg class="tick" viewBox="0 0 18 18"><circle cx="9" cy="9" r="9" fill="#fff"/><path d="M5 9.2l2.7 2.6L13 6.4" fill="none" stroke="#5f736d" stroke-width="2.2"/></svg>Pediatric Dentistry</li>
      <li><svg class="tick" viewBox="0 0 18 18"><circle cx="9" cy="9" r="9" fill="#fff"/><path d="M5 9.2l2.7 2.6L13 6.4" fill="none" stroke="#5f736d" stroke-width="2.2"/></svg>Teeth Whitening</li>
      <li><svg class="tick" viewBox="0 0 18 18"><circle cx="9" cy="9" r="9" fill="#fff"/><path d="M5 9.2l2.7 2.6L13 6.4" fill="none" stroke="#5f736d" stroke-width="2.2"/></svg>Dental Implants</li>
      <li><svg class="tick" viewBox="0 0 18 18"><circle cx="9" cy="9" r="9" fill="#fff"/><path d="M5 9.2l2.7 2.6L13 6.4" fill="none" stroke="#5f736d" stroke-width="2.2"/></svg>Wisdom Tooth Extraction</li>
      <li><svg class="tick" viewBox="0 0 18 18"><circle cx="9" cy="9" r="9" fill="#fff"/><path d="M5 9.2l2.7 2.6L13 6.4" fill="none" stroke="#5f736d" stroke-width="2.2"/></svg>Root Canal Therapy</li>
    </ul>
  </section>

  <section class="kids">
    <h2 class="kids__title">Silver Harbor Kids Treatment:</h2>
    <div class="kids__cols">
      <ul class="check-list">
        <li><svg class="tick" viewBox="0 0 18 18"><circle cx="9" cy="9" r="8" fill="#5f736d"/><path d="M5 9.2l2.7 2.6L13 6.4" fill="none" stroke="#fff" stroke-width="2"/></svg>Teeth Cleaning</li>
        <li><svg class="tick" viewBox="0 0 18 18"><circle cx="9" cy="9" r="8" fill="#5f736d"/><path d="M5 9.2l2.7 2.6L13 6.4" fill="none" stroke="#fff" stroke-width="2"/></svg>Flouride Application</li>
        <li><svg class="tick" viewBox="0 0 18 18"><circle cx="9" cy="9" r="8" fill="#5f736d"/><path d="M5 9.2l2.7 2.6L13 6.4" fill="none" stroke="#fff" stroke-width="2"/></svg>Tooth Colored Filing</li>
      </ul>
      <ul class="check-list">
        <li><svg class="tick" viewBox="0 0 18 18"><circle cx="9" cy="9" r="8" fill="#5f736d"/><path d="M5 9.2l2.7 2.6L13 6.4" fill="none" stroke="#fff" stroke-width="2"/></svg>Extraction</li>
        <li><svg class="tick" viewBox="0 0 18 18"><circle cx="9" cy="9" r="8" fill="#5f736d"/><path d="M5 9.2l2.7 2.6L13 6.4" fill="none" stroke="#fff" stroke-width="2"/></svg>Pit and Fissure Sealants</li>
        <li><svg class="tick" viewBox="0 0 18 18"><circle cx="9" cy="9" r="8" fill="#5f736d"/><path d="M5 9.2l2.7 2.6L13 6.4" fill="none" stroke="#fff" stroke-width="2"/></svg>Space Management</li>
      </ul>
    </div>
  </section>

  <footer class="footer">
    <p>#4821 Orchid Tower Makati Dalisay Cor. Verano St. Lumen Square .Makati</p>
    <p>Email: info@silverharbor.example.ph | mobile +639051274806 | Landline:(02)5162947 | <span class="footer__social"><span class="footer__mark"></span>@shdc.ph</span> | <span class="footer__social"><span class="footer__mark"></span>SHDC.ph</span></p>
  </footer>
</div>
</body>
</html>
```